Banner ad to sell prefabricated holiday homes in New Zealand

Harbourlight Homes build prefabricated homes in a factory that are then transported by truck to their site. It's coming into summer here in New Zealand and many people will be thinking about the holidays and wishing they had a holiday home.

The design should communicate some of the following benefits of our homes:
- Full project management
- Great value for money
- Delivered complete with all interior & exterior fittings
- Quality construction in our controlled factory

The banner ad will be displayed on a popular weather website www.skyreport.co.nz
Size: 760px x 120px
Would like it to be animated if but the size must be below 60kb.

I'll upload some nice holiday destination photos for backgrounds & some pictures of our holiday home designs for you to use.
Our main company colors are bright blue (pantone 3005) and light grey/silver.

Updatefor brief:
I would like the animation to show different text so that it's not all squashed up on the one image.
For example have "Prefabricated Holiday Homes" on one image & then it fades/changes to next image with "Delivered complete with all interior & exterior fittings". Or something like that with nice background images or pictures of our houses.

Font styles to use
Sans Serif

Colors
3176b5
0d5aa6
33a6d7
3276b5

Requirements
Nice to have
• Our logo

```html
<!DOCTYPE html>
<html lang="en">
<head>
<meta charset="utf-8">
<title>Harbourlight Homes – New Homes Made Easy</title>
<link rel="stylesheet" href="https://fonts.googleapis.com/css2?family=Oswald:wght@500&family=Arimo:wght@700&display=swap">
<style>
  :root {
    --blue-bright: #33a6d7;
    --blue-mid: #3276b5;
    --blue-deep: #0d5aa6;
    --headline: #8ff2ff;
    --white: #ffffff;
    --sky-top: #5c8fc4;
    --sky-low: #b9d3e6;
    --lawn: #6f9a3c;
    --logo-ink: #1f2d3a;
  }
  * { margin: 0; padding: 0; box-sizing: border-box; }
  html, body { width: 1200px; height: 189px; overflow: hidden; background: var(--white); }
  .banner {
    position: relative;
    width: 1200px;
    height: 189px;
    overflow: hidden;
    background: linear-gradient(180deg, #48b4e2 0%, var(--blue-bright) 45%, #2f9fd2 100%);
    font-family: "Arimo", Arial, sans-serif;
  }
  .house-photo {
    position: absolute;
    left: 0; top: 0;
    width: 372px; height: 189px;
    background: linear-gradient(180deg, var(--sky-top) 0%, var(--sky-low) 45%, #4d5a4e 62%, var(--lawn) 100%);
  }
  .headline {
    position: absolute;
    left: 392px; top: 42px;
    font-family: "Oswald", "Arial Narrow", sans-serif;
    font-weight: 500;
    font-size: 60px;
    line-height: 1;
    letter-spacing: 0.5px;
    color: var(--headline);
    text-transform: uppercase;
    white-space: nowrap;
  }
  .subline {
    position: absolute;
    left: 392px; top: 112px;
    font-size: 20px;
    font-weight: 700;
    color: var(--white);
    white-space: nowrap;
  }
  .corner {
    position: absolute;
    right: 0; top: 0;
  }
  .brand {
    position: absolute;
    right: 8px; top: 10px;
    width: 92px;
    display: flex;
    flex-direction: column;
    align-items: center;
    gap: 5px;
  }
  .brand-square {
    width: 28px; height: 28px;
    background: var(--blue-mid);
  }
  .brand-name {
    font-size: 10px;
    font-weight: 700;
    color: var(--logo-ink);
    text-align: center;
    line-height: 1.1;
  }
  .cta {
    position: absolute;
    left: 971px; top: 126px;
    width: 214px; height: 42px;
    border-radius: 6px;
    background: linear-gradient(180deg, #1f74c2 0%, var(--blue-deep) 100%);
    box-shadow: 0 2px 3px rgba(0, 40, 90, 0.35);
    display: flex;
    align-items: center;
    padding-left: 16px;
    color: var(--white);
    font-size: 17px;
    font-weight: 700;
    letter-spacing: 0.3px;
  }
  .cta-icon {
    position: absolute;
    right: 8px; top: 7px;
  }
</style>
</head>
<body>
  <div class="banner">
    <div class="house-photo" role="img" aria-label="Dark-clad single-storey prefabricated holiday home with a timber deck, lawn and mountains behind"></div>

    <h1 class="headline">New Homes Made Easy!</h1>
    <p class="subline">Delivered complete with all interior &amp; exterior fittings</p>

    <svg class="corner" width="140" height="90" viewBox="0 0 140 90" aria-hidden="true">
      <polygon points="0,0 140,0 140,90" fill="#ffffff"/>
    </svg>
    <div class="brand">
      <span class="brand-square"></span>
      <span class="brand-name">Harbourlight Homes</span>
    </div>

    <a class="cta">FIND OUT MORE
      <svg class="cta-icon" width="28" height="28" viewBox="0 0 28 28" aria-hidden="true">
        <circle cx="14" cy="14" r="13" fill="#ffffff"/>
        <path d="M11 8 L17 14 L11 20" fill="none" stroke="#0d5aa6" stroke-width="3" stroke-linecap="round" stroke-linejoin="round"/>
      </svg>
    </a>
  </div>
</body>
</html>
```